Kelvo Tech Oz Business card revamp

We are looking to revamp our business card design. We are hoping to change our colours to dark navey blue, gray, white and black but are open to keeping the same if a good design is submited. We are after somthing a bit differnt not just boring business card. I have attached a copy of our current card. We Want to keep the same logo design which i have attached a few to hopfully help you in this process. We are after a design that can be personalized to separate 4 people

Colors
0455a3
ffffff
000000
cbcbcb

Requirements
Must have
• Kelvo Tech Logo, address 3/41 Mallory Court, Wexhill 4218, phone number, Name and position

```html
<!DOCTYPE html>
<html lang="en">
<head>
<meta charset="utf-8">
<title>Kelvo Tech Business Cards</title>
<link rel="stylesheet" href="https://fonts.googleapis.com/css2?family=Open+Sans:wght@400;600;800&display=swap">
<style>
  :root {
    --stage: #d3d3d3;
    --card-white: #ffffff;
    --card-grey: #e9e9e9;
    --strip-grey: #ececec;
    --brand-blue: #1f7fc6;
    --brand-blue-light: #2b95d6;
    --ink-blue: #1e5f9c;
    --accent-orange: #f37a21;
  }
  * { box-sizing: border-box; margin: 0; padding: 0; }
  html, body {
    width: 1200px;
    height: 800px;
    overflow: hidden;
    background: var(--stage);
    font-family: "Open Sans", sans-serif;
  }
  .stage {
    width: 1200px;
    height: 800px;
    display: flex;
    align-items: center;
    justify-content: center;
    gap: 60px;
  }
  .card {
    position: relative;
    width: 525px;
    height: 300px;
    overflow: hidden;
    box-shadow: 0 14px 30px rgba(0, 0, 0, 0.18);
  }

  /* Front: personal details */
  .card-front { background: var(--card-white); }
  .side-strip {
    position: absolute;
    left: 0; top: 0;
    width: 38px; height: 100%;
    background: var(--strip-grey);
  }
  .name-marker {
    position: absolute;
    left: 22px; top: 104px;
    width: 32px; height: 30px;
    background: var(--brand-blue-light);
  }
  .holder-name {
    position: absolute;
    left: 66px; top: 102px;
    font-size: 25px;
    font-weight: 400;
    letter-spacing: 0.5px;
    color: var(--ink-blue);
    text-transform: uppercase;
    line-height: 34px;
  }
  .holder-role {
    position: absolute;
    left: 67px; top: 136px;
    font-size: 13px;
    font-weight: 600;
    letter-spacing: 1px;
    color: var(--ink-blue);
    text-transform: uppercase;
  }
  .contact-list {
    position: absolute;
    left: 48px; top: 164px;
    list-style: none;
    color: var(--ink-blue);
    font-size: 14px;
    line-height: 22px;
  }
  .contact-item { display: flex; align-items: center; gap: 10px; }
  .contact-icon { width: 13px; height: 13px; fill: var(--ink-blue); flex: none; }
  .accent-band {
    position: absolute;
    left: 318px; top: 178px;
    width: 207px; height: 24px;
    background: var(--brand-blue);
  }
  .front-brand {
    position: absolute;
    right: 26px; top: 34px;
    display: flex;
    align-items: center;
    gap: 8px;
  }

  /* Shared brand name */
  .brand-dot {
    border-radius: 50%;
    background: var(--accent-orange);
    flex: none;
  }
  .front-brand .brand-dot { width: 14px; height: 14px; }
  .brand-name {
    font-weight: 800;
    color: var(--brand-blue);
    white-space: nowrap;
  }
  .front-brand .brand-name { font-size: 22px; }

  /* Back: brand side */
  .card-back {
    background: var(--card-grey);
    display: flex;
    flex-direction: column;
    align-items: center;
    justify-content: center;
    gap: 34px;
  }
  .back-brand { display: flex; align-items: center; gap: 14px; }
  .back-brand .brand-dot { width: 34px; height: 34px; }
  .back-brand .brand-name { font-size: 52px; }
  .web-address {
    font-size: 15px;
    letter-spacing: 12px;
    color: var(--ink-blue);
    padding-left: 12px;
  }
</style>
</head>
<body>
<main class="stage">
  <section class="card card-front" aria-label="Business card front">
    <div class="side-strip"></div>
    <div class="name-marker"></div>
    <h1 class="holder-name">Marla J. Penrose</h1>
    <p class="holder-role">Project Manager</p>
    <ul class="contact-list">
      <li class="contact-item">
        <svg class="contact-icon" viewBox="0 0 24 24" aria-hidden="true"><path d="M12 1a8 8 0 0 0-8 8c0 6 8 14 8 14s8-8 8-14a8 8 0 0 0-8-8zm0 11a3 3 0 1 1 0-6 3 3 0 0 1 0 6z"/></svg>
        <span>3/41 Mallory Court, Wexhill 4218</span>
      </li>
      <li class="contact-item">
        <svg class="contact-icon" viewBox="0 0 24 24" aria-hidden="true"><path d="M6.6 10.8a15 15 0 0 0 6.6 6.6l2.2-2.2a1 1 0 0 1 1-.25 11.4 11.4 0 0 0 3.6.57 1 1 0 0 1 1 1V20a1 1 0 0 1-1 1A17 17 0 0 1 3 4a1 1 0 0 1 1-1h3.5a1 1 0 0 1 1 1c0 1.25.2 2.45.57 3.6a1 1 0 0 1-.25 1z"/></svg>
        <span>+1 555 013 2270</span>
      </li>
      <li class="contact-item">
        <svg class="contact-icon" viewBox="0 0 24 24" aria-hidden="true"><path d="M2 5h20v14H2zm2 2v.5l8 5 8-5V7l-8 5z"/></svg>
        <span>marla@kelvotech.com</span>
      </li>
    </ul>
    <div class="accent-band"></div>
    <div class="front-brand">
      <span class="brand-dot"></span>
      <span class="brand-name">Kelvo Tech</span>
    </div>
  </section>

  <section class="card card-back" aria-label="Business card back">
    <div class="back-brand">
      <span class="brand-dot"></span>
      <span class="brand-name">Kelvo Tech</span>
    </div>
    <p class="web-address">www.kelvotech.com</p>
  </section>
</main>
</body>
</html>
```